Home page for local retail aggregator

About us: We are a new company that showcases beautiful products available at nearby retail stores. This homepage is meant to display the latest products featured on our site and also allow the user to search, browse with filters, and access their account details.

Currently, our home page looks a little bland. We want the focus of the site to remain on the featured photos and products but the design should be more cohesive. The most successful designs will make more subtle use of our colors, provide intuitive menu controls, and look visually stunning.

This homepage has a few sections:

Header:
-Top Section: will always remain at the top of the page. There should be space for our company name ”zAntelope”, a tagline, and a place for the menus.
-Menus: user must be able to find links for: “My profile” “My Products” “Add Product” “Preview store”
-Bottom section: this will scroll with the user and always remain at the top of the screen providing access to a search box, and filters for “location” “price” and retail categories.

Main Page:
-Each product featured is shown on a tile that includes a photo, title, price, name of store, has space to leave a comment, and include counters for "likes," comments, and "Pods"). “Pods” are bookmark folders. The user’s profile pic is also shown in miniature if they leave a comment.

The final version of the site must be delivered in a fully layered photoshop file and have versions demonstrating what the page will look like both when a user is logged-in and when logged-out.

Target Market(s)

Most of our users are female 18-45. Our customers are retail store owners who want their products to look attractive and professional.

Industry/Entity Type

Retail

Requirements
Must have
• Our logo must be present on the site (attached to project). You're welcome to change the colors in the header but it should look good with our logo.

For reference here are colors we're currently using:
Site text is in Dark Blue: RGB(10/23/47)
Logo color on business cards is light blue: (51/153/204)
Nice to have
• Would love to see new versions of the menus that are more modern and intuitive. Currently we just have links to each individual control. Putting these in a drop-down or re-arranging them would be nice.

```html
<!DOCTYPE html>
<html lang="en">
<head>
<meta charset="utf-8">
<title>zAntelope – Local Product Search and Discovery</title>
<link href="https://fonts.googleapis.com/css2?family=Didact+Gothic&display=swap" rel="stylesheet">
<style>
  :root{
    --brand-blue:#0db1da;
    --band-top:#16aed8;
    --band-mid:#3fc2e4;
    --logo-ink:#3b6584;
    --nav-ink:#3d86ad;
    --title-ink:#1d3a56;
    --text-dark:#0a172f;
    --muted:#6f7a83;
    --pink:#ef1680;
    --card-bg:#e7edf0;
    --card-hi:#f2f5f6;
    --price-bg:#6b6b6b;
    --store-ink:#2a7ea8;
    --footer-bg:#ececec;
  }
  *{box-sizing:border-box;margin:0;padding:0}
  html,body{width:1200px;height:1200px;overflow:hidden;background:#fff}
  body{position:relative;font-family:"Didact Gothic",Arial,sans-serif;color:var(--text-dark)}

  .top-strip{position:absolute;left:138px;top:0;width:948px;height:10px;background:var(--brand-blue);border-radius:0 0 6px 6px}

  .brand{position:absolute;left:150px;top:30px}
  .brand-mark{position:absolute;left:24px;top:22px;width:96px;height:96px;border-radius:50%;background:var(--brand-blue)}
  .brand-name{position:absolute;left:128px;top:26px;font-size:44px;line-height:1;color:var(--logo-ink);letter-spacing:-1px;white-space:nowrap}
  .brand-tagline{position:absolute;left:133px;top:78px;font-size:15px;color:var(--muted);white-space:nowrap}

  .social{position:absolute;left:980px;top:20px;display:flex;gap:8px}
  .social span{width:28px;height:28px;background:#7cc3dc;border-radius:2px}

  .main-nav{position:absolute;left:642px;top:113px;display:flex;gap:20px;font-size:15px}
  .main-nav a{color:var(--nav-ink);text-decoration:none}
  .main-nav a:nth-child(3){margin-left:-4px}

  .search-band{position:absolute;left:0;top:193px;width:1200px;height:87px;
    background:linear-gradient(180deg,var(--band-top) 0%,var(--band-mid) 45%,var(--band-top) 100%);
    box-shadow:inset 0 -3px 4px rgba(0,0,0,.05)}
  .search-field{position:absolute;top:11px}
  .search-field label{display:block;color:#fff;font-size:15px;font-weight:bold;margin-left:1px;height:22px}
  .search-field .box{width:166px;height:39px;background:#fff;border-radius:4px;position:relative}
  .select-arrow{position:absolute;right:9px;top:15px;width:0;height:0;border-left:6px solid transparent;border-right:6px solid transparent;border-top:11px solid var(--brand-blue)}
  .go-btn{position:absolute;left:949px;top:33px;width:43px;height:38px;border-radius:4px;background:#e9edef;color:var(--band-top);font-weight:bold;font-size:18px;display:flex;align-items:center;justify-content:center}

  .product-grid{position:absolute;left:123px;top:316px;display:grid;grid-template-columns:repeat(4,233px);column-gap:12.7px;row-gap:19px}
  .product-card{position:relative;width:233px;height:318px;border-radius:6px;
    background:linear-gradient(160deg,var(--card-hi),var(--card-bg))}
  .product-title{position:absolute;left:15px;top:12px;font-size:14px;color:var(--title-ink);white-space:nowrap}
  .product-photo{position:absolute;left:16px;top:37px;width:201px;height:203px;box-shadow:0 0 2px rgba(0,0,0,.15)}
  .photo-lounge{background:linear-gradient(135deg,#cdb89a 0%,#efe3d2 35%,#f3e6ee 55%,#d7b99a 80%,#b99c79 100%)}
  .photo-purple{background:radial-gradient(ellipse 22% 48% at 50% 45%,#4b2a7e 0%,#5a3790 60%,#fff 100%)}
  .photo-black{background:radial-gradient(ellipse 18% 46% at 50% 45%,#111 0%,#222 60%,#fff 100%)}
  .photo-knit{background:radial-gradient(ellipse 22% 50% at 50% 45%,#f6f2ea 0%,#8a8a8a 55%,#fff 100%)}
  .price-tag{position:absolute;right:16px;top:192px;width:61px;height:48px;background:var(--price-bg);color:#fff;font-size:20px;display:flex;align-items:center;justify-content:center;font-family:Arial,sans-serif}
  .product-stats{position:absolute;left:15px;top:245px;display:flex;align-items:center;font-size:13px;color:var(--title-ink)}
  .product-stats svg{display:block;margin-right:1px}
  .product-stats .count{margin-right:3px}
  .store-name{position:absolute;right:18px;top:245px;font-family:Arial,sans-serif;font-size:12.5px;color:var(--store-ink)}
  .comment-row{position:absolute;left:15px;top:269px}
  .avatar{position:absolute;left:0;top:0;width:36px;height:38px;background:#fff}
  .avatar::after{content:"";position:absolute;left:9px;top:8px;width:18px;height:22px;border-radius:9px 9px 4px 4px;background:#d6d9db}
  .avatar.active::before{content:"";position:absolute;left:3px;bottom:0;width:33px;height:9px;background:#7dd6ee;z-index:1}
  .comment-box{position:absolute;left:42px;top:0;width:159px;height:38px;background:#fff;font-family:Arial,sans-serif;font-size:11px;color:#666;padding:13px 0 0 17px;white-space:nowrap}

  .site-footer{position:absolute;left:135px;top:1141px;width:948px;height:59px;background:var(--footer-bg);border-radius:8px 8px 0 0;text-align:center;padding-top:20px;font-size:14px;color:#2b3340}
  .site-footer a{color:var(--pink);text-decoration:none}
</style>
</head>
<body>
<svg width="0" height="0" style="position:absolute">
  <defs>
    <symbol id="icon-heart" viewBox="0 0 20 18"><path d="M10 17 C4 12 0 9 0 5 A5 5 0 0 1 10 3 A5 5 0 0 1 20 5 C20 9 16 12 10 17Z" fill="#ef1680"/></symbol>
    <symbol id="icon-comment" viewBox="0 0 20 17"><path d="M0 0H20V12H8L4 17V12H0Z" fill="#ef1680"/></symbol>
    <symbol id="icon-pod" viewBox="0 0 12 16"><path d="M0 0H12V16L6 10L0 16Z" fill="#ef1680"/></symbol>
  </defs>
</svg>

<div class="top-strip"></div>

<header class="brand">
  <div class="brand-mark" role="img" aria-label="zAntelope brand mark"></div>
  <div class="brand-name">zAntelope</div>
  <div class="brand-tagline">Local Product Search and Discovery</div>
</header>

<div class="social"><span></span><span></span></div>

<nav class="main-nav">
  <a href="#">My Profile</a>
  <a href="#">My Products</a>
  <a href="#">Add Product</a>
  <a href="#">Preview Store</a>
  <a href="#">Logout</a>
</nav>

<section class="search-band">
  <div class="search-field" style="left:233px"><label>Search for</label><div class="box"></div></div>
  <div class="search-field" style="left:413px"><label>Location</label><div class="box"></div></div>
  <div class="search-field" style="left:592px"><label>Price</label><div class="box"></div></div>
  <div class="search-field" style="left:772px"><label>Retail categories</label><div class="box"><span class="select-arrow"></span></div></div>
  <div class="go-btn">Go</div>
</section>

<main class="product-grid">
  <article class="product-card">
    <h3 class="product-title">Romantic Print Nightgown</h3>
    <div class="product-photo photo-lounge" role="img" aria-label="Model lounging in a floral print nightgown"></div>
    <div class="price-tag">$60</div>
    <div class="product-stats"><svg width="20" height="17"><use href="#icon-heart"/></svg><span class="count">25</span><svg width="20" height="17"><use href="#icon-comment"/></svg><span class="count">&nbsp;17</span><svg width="12" height="16"><use href="#icon-pod"/></svg><span class="count">09</span></div>
    <div class="store-name">Minimal</div>
    <div class="comment-row"><div class="avatar"></div><div class="comment-box">What do you think?</div></div>
  </article>
  <article class="product-card">
    <h3 class="product-title">Shawl Collar Dress</h3>
    <div class="product-photo photo-purple" role="img" aria-label="Purple shawl collar dress"></div>
    <div class="price-tag">$60</div>
    <div class="product-stats"><svg width="20" height="17"><use href="#icon-heart"/></svg><span class="count">25</span><svg width="20" height="17"><use href="#icon-comment"/></svg><span class="count">&nbsp;17</span><svg width="12" height="16"><use href="#icon-pod"/></svg><span class="count">09</span></div>
    <div class="store-name">Minimal</div>
    <div class="comment-row"><div class="avatar"></div><div class="comment-box">What do you think?</div></div>
  </article>
  <article class="product-card">
    <h3 class="product-title">Metalic Sweater</h3>
    <div class="product-photo photo-knit" role="img" aria-label="Cream and grey knit sweater dress"></div>
    <div class="price-tag">$60</div>
    <div class="product-stats"><svg width="20" height="17"><use href="#icon-heart"/></svg><span class="count">25</span><svg width="20" height="17"><use href="#icon-comment"/></svg><span class="count">&nbsp;17</span><svg width="12" height="16"><use href="#icon-pod"/></svg><span class="count">09</span></div>
    <div class="store-name">Minimal</div>
    <div class="comment-row"><div class="avatar"></div><div class="comment-box">What do you think?</div></div>
  </article>
  <article class="product-card">
    <h3 class="product-title">Romantic Print Nightgown</h3>
    <div class="product-photo photo-black" role="img" aria-label="Black sleeveless dress"></div>
    <div class="price-tag">$60</div>
    <div class="product-stats"><svg width="20" height="17"><use href="#icon-heart"/></svg><span class="count">25</span><svg width="20" height="17"><use href="#icon-comment"/></svg><span class="count">&nbsp;17</span><svg width="12" height="16"><use href="#icon-pod"/></svg><span class="count">09</span></div>
    <div class="store-name">Minimal</div>
    <div class="comment-row"><div class="avatar active"></div><div class="comment-box">What do you think?</div></div>
  </article>

  <article class="product-card">
    <h3 class="product-title">Metalic Sweater</h3>
    <div class="product-photo photo-knit" role="img" aria-label="Cream and grey knit sweater dress"></div>
    <div class="price-tag">$60</div>
    <div class="product-stats"><svg width="20" height="17"><use href="#icon-heart"/></svg><span class="count">25</span><svg width="20" height="17"><use href="#icon-comment"/></svg><span class="count">&nbsp;17</span><svg width="12" height="16"><use href="#icon-pod"/></svg><span class="count">09</span></div>
    <div class="store-name">Minimal</div>
    <div class="comment-row"><div class="avatar"></div><div class="comment-box">What do you think?</div></div>
  </article>
  <article class="product-card">
    <h3 class="product-title">Romantic Print Nightgown</h3>
    <div class="product-photo photo-black" role="img" aria-label="Black sleeveless dress"></div>
    <div class="price-tag">$60</div>
    <div class="product-stats"><svg width="20" height="17"><use href="#icon-heart"/></svg><span class="count">25</span><svg width="20" height="17"><use href="#icon-comment"/></svg><span class="count">&nbsp;17</span><svg width="12" height="16"><use href="#icon-pod"/></svg><span class="count">09</span></div>
    <div class="store-name">Minimal</div>
    <div class="comment-row"><div class="avatar"></div><div class="comment-box">What do you think?</div></div>
  </article>
  <article class="product-card">
    <h3 class="product-title">Romantic Print Nightgown</h3>
    <div class="product-photo photo-lounge" role="img" aria-label="Model lounging in a floral print nightgown"></div>
    <div class="price-tag">$60</div>
    <div class="product-stats"><svg width="20" height="17"><use href="#icon-heart"/></svg><span class="count">25</span><svg width="20" height="17"><use href="#icon-comment"/></svg><span class="count">&nbsp;17</span><svg width="12" height="16"><use href="#icon-pod"/></svg><span class="count">09</span></div>
    <div class="store-name">Minimal</div>
    <div class="comment-row"><div class="avatar"></div><div class="comment-box">What do you think?</div></div>
  </article>
  <article class="product-card">
    <h3 class="product-title">Shawl Collar Dress</h3>
    <div class="product-photo photo-purple" role="img" aria-label="Purple shawl collar dress"></div>
    <div class="price-tag">$60</div>
    <div class="product-stats"><svg width="20" height="17"><use href="#icon-heart"/></svg><span class="count">25</span><svg width="20" height="17"><use href="#icon-comment"/></svg><span class="count">&nbsp;17</span><svg width="12" height="16"><use href="#icon-pod"/></svg><span class="count">09</span></div>
    <div class="store-name">Minimal</div>
    <div class="comment-row"><div class="avatar"></div><div class="comment-box">What do you think?</div></div>
  </article>
</main>

<footer class="site-footer">Copyright &nbsp;2012 zAntelope - Discover beautiful products available locally <a href="#">Privacy</a></footer>
</body>
</html>
```